Harbor Print Studio gallery website

I need a Website for a gallery with a shopify integration or maybe even better also compatible with squarespace.
the website should have following riders: Künstler, Veranstaltungen, Shop, About Us.
some nice examples for inspiration of the website architecture are:
https://www.tarnelgalerie.com/
https://www.mossline-gallery.com/de/
https://zinnbergalerie.de/
It should be easy for us to make adaptations and fill the website with new content.
Attached there is the CI an logo for the brand.
Art Collectors,
artgallery
3 page

```html
<!DOCTYPE html>
<html lang="en">
<head>
<meta charset="utf-8">
<title>Harbor Print Studio</title>
<link href="https://fonts.googleapis.com/css2?family=Montserrat:wght@300;400;500;600;700&display=swap" rel="stylesheet">
<style>
:root{
  --black:#000;
  --ink:#0b0b0b;
  --panel:#161616;
  --card:#1c1c1c;
  --red:#c1121f;
  --red-bright:#d4141f;
  --white:#fff;
  --grey:#cfcfcf;
  --muted:#9a9a9a;
}
*{margin:0;padding:0;box-sizing:border-box}
html,body{width:1200px;height:3560px;overflow:hidden;background:var(--black)}
body{position:relative;font-family:'Montserrat',sans-serif;color:var(--white)}
.abs{position:absolute}
.center-text{text-align:center;left:0;width:1200px}

/* header */
.site-nav a{position:absolute;top:51px;font-size:13px;color:var(--white);text-decoration:none;letter-spacing:.3px;transform:translateX(-50%)}
.nav-active::after{content:"";position:absolute;left:50%;top:22px;width:20px;height:2px;background:var(--white);transform:translateX(-50%)}
.brand{position:absolute;left:0;width:1200px;text-align:center;font-weight:400;letter-spacing:.5px;color:var(--white)}
.brand-square{display:block;margin:0 auto;border:2px solid var(--red)}

/* hero */
.hero{left:0;top:0;width:1200px;height:665px;
  background:
   radial-gradient(ellipse at 70% 35%,rgba(230,205,170,.55),transparent 55%),
   linear-gradient(180deg,#1b1a1a 0%,#4a4038 45%,#7a5c42 75%,#3a2a1e 100%)}
.hero-shade{left:0;top:0;width:1200px;height:665px;background:linear-gradient(90deg,rgba(0,0,0,.75) 0%,rgba(0,0,0,.25) 45%,rgba(0,0,0,0) 100%)}
.hero-box{left:148px;top:217px;width:405px;height:238px;border:1px solid var(--red);background:rgba(10,10,10,.55)}
.corner-tl{left:148px;top:214px;width:48px;height:4px;background:var(--red)}
.corner-br{left:550px;top:412px;width:4px;height:46px;background:var(--red)}
.corner-br2{left:506px;top:454px;width:48px;height:4px;background:var(--red)}
.hero-kicker{left:148px;width:405px;top:250px;text-align:center;font-size:19px;font-weight:400}
.hero-title{left:148px;width:405px;top:276px;text-align:center;font-size:40px;font-weight:400;line-height:43px}
.hero-text{left:190px;width:320px;top:368px;text-align:center;font-size:12px;line-height:22px;color:var(--grey)}
.btn-red{background:var(--red);color:var(--white);font-weight:700;font-size:12px;text-align:center;letter-spacing:.3px}
.hero-btn{left:279px;top:437px;width:148px;height:37px;line-height:37px}
.arrow{top:312px}

/* section titles */
.kicker{font-size:13px;color:var(--red);letter-spacing:.3px;font-weight:400}
.title{font-size:33px;font-weight:400;letter-spacing:.3px}
.rule{height:2px;width:70px;background:var(--red)}

/* gallery */
.tile{position:absolute;width:245px}
.view-btn{left:505px;top:1459px;width:197px;height:41px;line-height:41px}

/* about */
.about{left:0;top:1560px;width:1200px;height:649px;background:radial-gradient(ellipse at 50% 100%,#2a2a2a 0%,var(--panel) 45%,#0f0f0f 100%)}
.frame-red{border:6px solid var(--red)}
.frame-white{border:5px solid #e9e9e9}
.about-text{left:655px;width:430px;font-size:14px;line-height:23px;color:var(--grey)}
.btn-outline{left:655px;top:2018px;width:159px;height:39px;line-height:37px;border:1px solid var(--red);color:var(--red);font-size:11px;font-weight:600;text-align:center}

/* shop */
.shop-bg{left:0;top:2209px;width:1200px;height:1351px;background:linear-gradient(180deg,#000 0%,#000 25%,#0d0d0d 45%,#121212 70%,#0a0a0a 100%)}
.shop-card{width:386px;height:124px;background:var(--card);border:1px solid #2a2a2a;text-align:center}
.shop-card h3{margin-top:24px;font-size:14px;font-weight:400;letter-spacing:.3px}
.shop-card p{margin:4px auto 0;width:340px;font-size:10px;line-height:17px;color:var(--grey)}
.shop-card span{display:block;margin:10px auto 0;width:32px;height:2px;background:var(--red)}

/* newsletter */
.news-box{left:169px;top:2924px;width:860px;height:339px;border:1px solid var(--red);background:#121212}
.news-text{font-size:12px;line-height:17px;color:var(--grey)}
.email{left:394px;top:3127px;width:419px;height:43px;border:1px solid #bdbdbd;background:#0d0d0d}
.email span{position:absolute;left:18px;top:13px;font-size:11px;color:var(--grey)}
.subscribe{left:691px;top:3131px;width:116px;height:35px;line-height:35px;font-size:10px}

/* footer */
.foot-nav a{position:absolute;top:3390px;font-size:13px;color:var(--white);text-decoration:none;transform:translateX(-50%)}
.dot{width:4px;height:4px;background:var(--red);border-radius:50%}
.copyright{top:3458px;font-size:11px;color:var(--grey)}
.social{top:3498px;width:22px;height:22px;border-radius:50%;border:2px solid var(--white)}
</style>
</head>
<body>

<!-- hero -->
<div class="abs hero" role="img" aria-label="Photograph of a gallery room with colourful abstract paintings hung on lit walls"></div>
<div class="abs hero-shade"></div>

<nav class="site-nav">
  <a href="#" class="nav-active" style="left:252px">ARTITSTS</a>
  <a href="#" style="left:381px">EVENTS</a>
  <a href="#" style="left:824px">SHOP</a>
  <a href="#" style="left:951px">ABOUT US</a>
</nav>
<div class="brand" style="top:72px;font-size:18px">HARBOR PRINT STUDIO</div>
<span class="abs brand-square" style="left:594px;top:104px;width:11px;height:11px"></span>

<div class="abs hero-box"></div>
<div class="abs corner-tl"></div>
<div class="abs corner-br"></div>
<div class="abs corner-br2"></div>
<div class="abs hero-kicker">WE HAVE A</div>
<h1 class="abs hero-title">FINE ART WORK<br>EDITIONS</h1>
<p class="abs hero-text">Lorem ipsum dolor sit amet, consectetur adipisc-ing elit, sed do eiusmod tempor</p>
<div class="abs btn-red hero-btn">LEARN MORE</div>

<svg class="abs arrow" style="left:40px" width="18" height="32" viewBox="0 0 18 32"><polyline points="16,2 2,16 16,30" fill="none" stroke="#fff" stroke-width="2.5"/></svg>
<svg class="abs arrow" style="left:1148px" width="18" height="32" viewBox="0 0 18 32"><polyline points="2,2 16,16 2,30" fill="none" stroke="#fff" stroke-width="2.5"/></svg>

<!-- gallery -->
<div class="abs" style="left:599px;top:665px;width:1px;height:42px;background:#555"></div>
<div class="abs center-text kicker" style="top:714px">GALLERY</div>
<h2 class="abs center-text title" style="top:738px">OUR ARTWORK</h2>
<div class="abs rule" style="left:565px;top:787px"></div>

<div class="abs" style="left:105px;top:1124px;width:245px;height:297px;background:#141414"></div>
<div class="tile" style="left:105px;top:835px;height:289px;background:linear-gradient(160deg,#e7b36a,#5d7a3a 55%,#c9a06a)" role="img" aria-label="Landscape painting of cypress trees on a hillside path"></div>
<div class="tile" style="left:105px;top:1131px;height:238px;background:linear-gradient(160deg,#2a3e6b,#a8431f 55%,#1d3a7a)" role="img" aria-label="Painting of sailing ships in a harbour at night"></div>
<div class="tile" style="left:357px;top:835px;height:156px;background:linear-gradient(160deg,#6fa4a8,#b7b15e 55%,#3d6a6e)" role="img" aria-label="Painting of a canal city with boats"></div>
<div class="tile" style="left:357px;top:998px;height:263px;background:linear-gradient(170deg,#5a6fa8,#e2733d 45%,#f3b64c 65%,#3e8cab)" role="img" aria-label="Painting of a sailboat at sunset"></div>
<div class="tile" style="left:357px;top:1268px;height:153px;background:linear-gradient(160deg,#4b5e45,#6e5c78 50%,#2f4636)" role="img" aria-label="Painting of water lilies on a pond"></div>
<div class="tile" style="left:612px;top:835px;height:289px;background:linear-gradient(170deg,#d8d4cc,#6f665c 55%,#3b342c)" role="img" aria-label="Abstract textured painting of a city skyline"></div>
<div class="tile" style="left:612px;top:1131px;height:290px;background:linear-gradient(140deg,#1f3f9a,#c7312a 45%,#e8b43a 70%,#1c2c6a)" role="img" aria-label="Colourful expressive portrait painting"></div>
<div class="tile" style="left:864px;top:835px;height:289px;background:linear-gradient(160deg,#f2a11c,#f7c52a 45%,#2e9ab2 70%,#e9582a)" role="img" aria-label="Abstract painting in yellow, orange and turquoise"></div>
<div class="tile" style="left:864px;top:1131px;height:290px;background:linear-gradient(175deg,#b566b9,#ec6a3e 40%,#f4b13f 60%,#6a79b8)" role="img" aria-label="Painting of a colourful lakeside sunset"></div>

<div class="abs btn-red view-btn">VIEW ALL ARTWORK</div>

<!-- about -->
<div class="abs about"></div>
<div class="abs frame-red" style="left:169px;top:1637px;width:308px;height:254px;background:linear-gradient(160deg,#1c3a7a,#3d6b4a 45%,#d98ad6 70%,#e8a33c)" role="img" aria-label="Painting of a pink lotus flower"></div>
<div class="abs frame-white" style="left:507px;top:1824px;width:83px;height:67px;background:linear-gradient(160deg,#cfcfcf,#4d3a2e 60%,#a8442a)" role="img" aria-label="Small framed print"></div>
<div class="abs frame-red" style="left:507px;top:1919px;width:45px;height:36px;border-width:5px"></div>
<div class="abs frame-red" style="left:207px;top:1917px;width:195px;height:162px;background:linear-gradient(160deg,#1f5a7a,#3a3a3a 45%,#c59b4a 70%,#1e3a5a)" role="img" aria-label="Painting of an elephant with colourful ears"></div>
<div class="abs frame-white" style="left:434px;top:1949px;width:44px;height:38px;border-width:6px"></div>
<div class="abs frame-white" style="left:434px;top:2013px;width:119px;height:98px;background:linear-gradient(180deg,#2b4e8a,#e46a3a 55%,#f0a86a)" role="img" aria-label="Small framed sunset painting"></div>

<div class="abs kicker" style="left:653px;top:1681px">WHO WE ARE</div>
<h2 class="abs title" style="left:653px;top:1700px;line-height:39px">ABOUT HARBOR<br>PRINT STUDIO</h2>
<div class="abs rule" style="left:655px;top:1789px"></div>
<p class="abs about-text" style="top:1808px">Lorem ipsum dolor sit amet, consectetur adipiscing elit, sed do eiusmod tempor incididunt ut labore et dolore magna aliqua. Quis ipsum suspendisse ultrices gravida. Risus com-modo viverra maecenas accumsan lacus vel</p>
<p class="abs about-text" style="top:1923px">Aacilisis. Lorem ipsum dolor sit amet, consectetur adipiscing elit, sed do eiusmod tempor incididunt ut labore et dolore magna aliqua. Quis ipsum suspendisse</p>
<div class="abs btn-outline">LEARN MORE</div>

<!-- shop -->
<div class="abs shop-bg"></div>
<div class="abs center-text kicker" style="top:2287px">FEATURED</div>
<h2 class="abs center-text title" style="top:2301px">SHOP OUR ART</h2>
<div class="abs rule" style="left:565px;top:2351px"></div>

<div class="abs" style="left:149px;top:2403px;width:430px;height:287px;background:linear-gradient(180deg,#8a8680,#54504a 55%,#2b2620)" role="img" aria-label="Photograph of a long gallery hall with pop art and a sculpture"></div>
<div class="abs" style="left:603px;top:2403px;width:431px;height:287px;background:linear-gradient(180deg,#6a3e22,#a8582e 50%,#4a2a18)" role="img" aria-label="Photograph of a warm-lit gallery room with many colourful canvases"></div>
<div class="abs shop-card" style="left:173px;top:2630px">
  <h3>LOREM IPSUM DOLOR SIT AMET</h3>
  <p>Aonsectetur adipiscing elit, sed do eiusmod tempor incididunt ut labore et dolore magna aliqua Quis ipsum</p>
  <span></span>
</div>
<div class="abs shop-card" style="left:636px;top:2630px;width:365px">
  <h3>LOREM IPSUM DOLOR SIT AMET</h3>
  <p>Aonsectetur adipiscing elit, sed do eiusmod tempor incididunt ut labore et dolore magna aliqua Quis ipsum</p>
  <span></span>
</div>

<!-- newsletter -->
<div class="abs news-box"></div>
<div class="abs" style="left:163px;top:2917px;width:76px;height:6px;background:var(--red)"></div>
<div class="abs" style="left:163px;top:2917px;width:6px;height:70px;background:var(--red)"></div>
<div class="abs" style="left:1029px;top:3196px;width:6px;height:74px;background:var(--red)"></div>
<div class="abs" style="left:955px;top:3264px;width:80px;height:6px;background:var(--red)"></div>
<div class="abs center-text kicker" style="top:2990px">SIGN UP EMAIL</div>
<h2 class="abs center-text title" style="top:3005px;font-size:31px">NEWSLETTER SIGN UP</h2>
<p class="abs center-text news-text" style="top:3069px">With our newsletter you won't miss any exhibitions. You will also receive<br>special offers and always receive the latest news.</p>
<div class="abs email"><span>Email address</span></div>
<div class="abs btn-red subscribe">SUBSCRIBE</div>

<!-- footer -->
<nav class="foot-nav">
  <a href="#" style="left:250px">ARTISTS</a>
  <a href="#" style="left:386px">EVENTS</a>
  <a href="#" style="left:799px">SHOP</a>
  <a href="#" style="left:937px">ABOUT US</a>
</nav>
<div class="abs dot" style="left:317px;top:3398px"></div>
<div class="abs dot" style="left:863px;top:3398px"></div>
<div class="brand" style="top:3387px;font-size:21px">HARBOR PRINT STUDIO</div>
<span class="abs brand-square" style="left:594px;top:3426px;width:12px;height:12px"></span>
<div class="abs center-text copyright">Copyright © 2024 Harbor Print Studio Hamburg. All Right Reserved</div>
<div class="abs social" style="left:523px;border-color:var(--red)"></div>
<div class="abs social" style="left:563px"></div>
<div class="abs social" style="left:608px"></div>
<div class="abs social" style="left:654px"></div>

</body>
</html>
```